New web design needed for our company

We need our website designing, it needs to be professional and look creative,
We are a plumbing and heating company called Brackwell Flow's (www.brackwellflows.co.uk)
I like this site design also some of the following maybe:
https://www.tindermoorwarmth.com/
http://www.quorvapower.co.uk

Please let me know when you want our logo files as it wont let me upload them

The design will require coding once the design is complete, i havent paid for this yet as i want to be sure the design is good before i commit.

The template needs to look professional and look like one of the leading companies.
The site will consist of all the features this site has https://www.tindermoorwarmth.com/

I like a modern design with the latest technology.

Must have a customer login page and a my account area

Target Market(s)

Everyone

Industry/Entity Type

Plumbing

Coding

Coded - Design and coding required

Number of Pages Required

5+ page

Font styles to use
Other font styles liked:
• whatever suites

Requirements
Must have
• The design will require coding once the design is complete, i havent paid for this yet as i want to be sure the design is good before i commit.
• The template needs to look professional and look like one of the leading companies.
• The site will consist of all the features this site has https://www.tindermoorwarmth.com/
• I like a modern design with the latest technology.
• Must have a customer login page and a my account area
Nice to have
• inspirational and different
Should not have
• plain boring designs like most plumbing websites, needs to be inspiring and attract people from first sight.

```html
<!DOCTYPE html>
<html lang="en">
<head>
<meta charset="utf-8">
<title>Brackwell Flow's – Plumbing & Heating</title>
<link rel="stylesheet" href="https://fonts.googleapis.com/css2?family=Open+Sans:wght@400;600;700&display=swap">
<style>
:root{
  --navy:#1b2e5e;
  --hero-a:#1a3b7c;
  --hero-b:#14285a;
  --band:#1f4183;
  --accent:#f0593f;
  --ink:#333;
  --muted:#777;
  --grey-bg:#eeeeee;
  --footer:#333333;
  --footer-base:#262626;
  --white:#fff;
}
*{box-sizing:border-box;margin:0;padding:0}
html,body{width:676px;height:1200px;overflow:hidden}
body{font-family:"Open Sans",Arial,sans-serif;color:var(--ink);background:var(--white);position:relative}
.topbar{height:23px;background:var(--navy);color:var(--white);font-size:7.5px;display:flex;align-items:center;padding:0 53px;gap:22px}
.topbar .right{margin-left:auto;display:flex;gap:20px}
.topbar span{display:flex;align-items:center;gap:5px}
.header{height:44px;display:flex;align-items:center;padding:0 52px;border-bottom:1px solid #e4e4e4}
.brand{display:flex;align-items:center;gap:6px;font-size:19px;font-weight:700;color:var(--navy);letter-spacing:-.3px}
.brand i{width:12px;height:12px;border-radius:50%;background:var(--accent);display:block}
.nav{margin-left:auto;display:flex;gap:18px;font-size:7.5px;color:#666}
.nav .active{color:var(--accent)}
.hero{height:244px;background:linear-gradient(135deg,var(--hero-a),var(--hero-b) 60%,#0f214c);text-align:center;color:var(--white);padding-top:45px}
.hero h1{font-weight:400;font-size:33px;line-height:43px}
.btn-outline{display:inline-block;margin-top:22px;width:138px;height:34px;line-height:31px;border:2px solid var(--accent);border-radius:2px;font-size:17px}
.question{height:62px;background:var(--band);display:flex;align-items:center;padding:0 52px}
.question h3{color:var(--accent);font-weight:400;font-size:12px}
.question p{color:var(--white);font-weight:700;font-size:10.5px;margin-top:1px}
.btn-solid{margin-left:auto;background:var(--accent);color:var(--white);font-size:10px;width:91px;height:22px;line-height:22px;text-align:center;border-radius:2px}
.tasks{background:var(--grey-bg);height:507px;padding-top:22px;text-align:center}
.tasks h2,.clients h2{font-size:18px;font-weight:600;color:var(--ink)}
.tasks .lead{font-size:8px;color:var(--muted);line-height:15px;margin:14px auto 0;width:400px}
.options{display:flex;justify-content:space-between;padding:0 46px 0 40px;margin-top:30px}
.option{width:90px;display:flex;flex-direction:column;align-items:center;font-size:10px;color:#555;line-height:12px}
.option .label{height:30px;display:flex;align-items:flex-start}
.option.active .label{color:var(--navy);padding-top:4px}
.option .icon{width:64px;height:64px;border-radius:50%;display:flex;align-items:center;justify-content:center;margin-top:2px}
.option.active .icon{background:#f6f6f6}
.services-title{margin-top:28px}
.cards{display:flex;gap:16px;padding:0 52px;margin-top:22px}
.card{width:180px;height:196px;background:var(--white);padding:10px}
.card .photo{height:145px}
.card p{font-size:10px;font-weight:600;margin:10px 0 0 2px;text-align:left}
.clients{height:127px;text-align:center;padding-top:33px}
.logos{display:flex;justify-content:space-around;padding:0 40px;margin-top:14px;font-size:22px;font-weight:700;color:#8a8a8a}
.footer{background:var(--footer);height:156px;color:#ddd;display:flex;padding:28px 0 0 57px;font-size:7.5px}
.footer .col{width:152px}
.footer .col:nth-child(3){width:138px}
.footer h4{font-size:8px;font-weight:700;color:var(--white)}
.footer h4::after{content:"";display:block;width:32px;height:1px;background:#aaa;margin-top:8px}
.footer ul{list-style:none;margin-top:11px}
.footer li{height:14.6px}
.footer li.current{color:var(--accent)}
.social{display:flex;gap:11px;margin-top:12px}
.social i{width:9px;height:9px;border-radius:50%;background:#ddd;display:block}
.social i:first-child{background:var(--accent)}
.base{height:37px;background:var(--footer-base);color:#ddd;font-size:7.5px;text-align:center;line-height:37px}
</style>
</head>
<body>
<div class="topbar">
  <span><svg width="8" height="6" viewBox="0 0 8 6"><rect width="8" height="6" fill="#fff"/><path d="M0 0l4 3 4-3" stroke="#1b2e5e" fill="none"/></svg>hello@brackwellmail.com</span>
  <span><svg width="7" height="7" viewBox="0 0 10 10"><path d="M2 0l2 3-1 1.5c.8 1.5 1.8 2.5 3 3L7.5 6 10 8 8.5 10C4 9.5.5 6 0 1.5z" fill="#fff"/></svg>Call Us :+08172950</span>
  <div class="right">
    <span><svg width="6" height="8" viewBox="0 0 6 8"><rect y="3" width="6" height="5" fill="#fff"/><path d="M1.3 3.5V2a1.7 1.7 0 013.4 0v1.5" stroke="#fff" fill="none"/></svg>Sign In</span>
    <span><svg width="7" height="8" viewBox="0 0 7 8"><circle cx="3.5" cy="2" r="2" fill="#fff"/><path d="M0 8a3.5 3.5 0 017 0z" fill="#fff"/></svg>Register</span>
  </div>
</div>
<header class="header">
  <div class="brand"><i></i>Brackwell Flow's</div>
  <nav class="nav"><span class="active">Home</span><span>About</span><span>Services</span><span>Emergencies Business</span><span>Customers</span><span>Pro Care</span><span>Help and Support</span></nav>
</header>
<section class="hero">
  <h1>Lorem ipsum dolor sit ame<br>ectetur adipis</h1>
  <a class="btn-outline">View All</a>
</section>
<section class="question">
  <div><h3>Got a Question?</h3><p>Our online frequently asked questions offers a wide host of answers which may help</p></div>
  <a class="btn-solid">Get a quote</a>
</section>
<section class="tasks">
  <h2>What are you looking to do?</h2>
  <p class="lead">Unique features give you a head-start over your competitors: countless customization options, working forms and newsletters, flexible code, great design, and more</p>
  <div class="options">
    <div class="option active"><div class="label">Pay your bil</div><div class="icon"><svg width="28" height="40" viewBox="0 0 28 40"><rect x="5" y="2" width="16" height="28" rx="2" fill="none" stroke="#f0593f" stroke-width="2"/><circle cx="13" cy="14" r="4" fill="#f0593f"/><path d="M14 30v8h10V24l-5-4" fill="#f7a596"/></svg></div></div>
    <div class="option"><div class="label">I need a landlord certificate</div><div class="icon"><svg width="42" height="34" viewBox="0 0 42 34"><rect x="1" y="1" width="36" height="26" fill="none" stroke="#f0593f" stroke-width="2"/><path d="M6 8h20M6 13h16M6 18h12" stroke="#f0593f" stroke-width="2"/><circle cx="31" cy="22" r="6" fill="#f0593f"/><circle cx="31" cy="22" r="2.5" fill="#eee"/></svg></div></div>
    <div class="option"><div class="label">Manage your account</div><div class="icon"><svg width="46" height="32" viewBox="0 0 46 32"><rect x="7" y="2" width="32" height="22" fill="none" stroke="#f0593f" stroke-width="2.5"/><path d="M1 27h44l-3 4H4z" fill="#f0593f"/></svg></div></div>
    <div class="option"><div class="label">Need a boiler service</div><div class="icon"><svg width="36" height="36" viewBox="0 0 36 36"><path d="M4 4l28 28M32 4L4 32" stroke="#f0593f" stroke-width="4" stroke-linecap="round"/><circle cx="6" cy="6" r="5" fill="none" stroke="#f0593f" stroke-width="2"/></svg></div></div>
    <div class="option"><div class="label">Set Up a Direct Debit</div><div class="icon"><svg width="34" height="34" viewBox="0 0 34 34"><circle cx="17" cy="17" r="15" fill="#f0593f"/></svg></div></div>
    <div class="option"><div class="label">Book an engineer</div><div class="icon"><svg width="34" height="34" viewBox="0 0 34 34"><rect x="2" y="5" width="30" height="27" rx="2" fill="none" stroke="#f0593f" stroke-width="2.5"/><path d="M2 11h30" stroke="#f0593f" stroke-width="3"/><path d="M9 1v7M25 1v7" stroke="#f0593f" stroke-width="2.5"/><g fill="#f0593f"><rect x="7" y="15" width="4" height="4"/><rect x="15" y="15" width="4" height="4"/><rect x="23" y="15" width="4" height="4"/><rect x="7" y="23" width="4" height="4"/><rect x="15" y="23" width="4" height="4"/><rect x="23" y="23" width="4" height="4"/></g></svg></div></div>
  </div>
  <h2 class="services-title">Our Services</h2>
  <div class="cards">
    <div class="card"><div class="photo" role="img" aria-label="Plumber fixing pipework under a kitchen sink" style="background:linear-gradient(160deg,#e4e6ea,#9aa3b3 60%,#3b4f86)"></div><p>Lorem ipsum dolor sit amet</p></div>
    <div class="card"><div class="photo" role="img" aria-label="Engineer servicing a wall-mounted water heater" style="background:linear-gradient(160deg,#f1f1f1,#c9c3b8 60%,#8a7a62)"></div><p>Lorem ipsum dolor sit amet</p></div>
    <div class="card"><div class="photo" role="img" aria-label="Plumber measuring white pipework" style="background:linear-gradient(160deg,#d9d4ce,#b39a86 55%,#6b6660)"></div><p>Lorem ipsum dolor sit amet</p></div>
  </div>
</section>
<section class="clients">
  <h2>Satisfied Clients</h2>
  <div class="logos"><span>Fenmark</span><span>Fenmark</span><span>Fenmark</span><span>Fenmark</span><span>Fenmark</span></div>
</section>
<footer class="footer">
  <div class="col"><h4>INFORMATIONS</h4><ul><li class="current">Home</li><li>Our Guarantee</li><li>Charges</li><li>My Bill</li><li>Emergencies</li><li>Got a problem?</li></ul></div>
  <div class="col"><h4>CUSTOMER CARE</h4><ul><li>Contact Us</li><li>Site Map</li><li>Top Sales &amp; Bestsellers</li><li>Gift Vouchers</li><li>Best Sellers</li></ul></div>
  <div class="col"><h4>YOUR ACCOUNT</h4><ul><li>Order Status</li><li>My Wishlist</li><li>Delivery Address</li><li>Order History</li><li>Newsletter</li></ul></div>
  <div class="col"><h4>GET IN TOUCH</h4><ul><li style="height:17.6px">Harlow Supply Shop</li><li style="height:17.6px">Mill Lane 48, Orton Centre</li><li>(011) 348 560 71</li></ul><div class="social"><i></i><i></i><i></i><i></i><i></i><i></i></div></div>
</footer>
<div class="base">© 2016 Brackwell Flow's UK Limited, All rights reserved.</div>
</body>
</html>
```